5 Piece Complete C.D. Artwork for Country Music Duo

We need the complete 5 piece artwork designed for our C.D. (Front, Back, Inside R, Inside L, C.D. Cover), as directed by the specifications from Brightwell Disc Pressers.

We are a contemporary country/singer songwriter duo from Alberta looking to communicate a modern, sleek, unique, vibe from this album called "Harbors". Our songs are catchy, fun, and commercial; consistent with what is on top 40 country radio.

We would like to see creative, eye catching designs. We'd like to still have our faces visible and clear, please. We've been doing our own artwork, and are excited to see what you guys come up with.

- - - - We've included several photos. For the Album Cover image, we prefer "Copper Sparrow Main photo Edit", but included others in case you have ideas, perhaps for the inside flaps.

- - - - Digipack Template included in Uploaded files.

Target Market(s)

Men & Women between the ages of 18-45.
Fans of modern country music (Danna Belcourt; Rusty Ferngate, etc)

Industry/Entity Type

Music Download

Requirements
Must have
• - Must conform to the specifications in the Brightwell digipack template
• - An image of the duo on the cover
• - The band name (Copper Sparrow) & Album Name (Harbors)
Nice to have
• - washes of light, colour
• - "Copper Sparrow" font to be simple, if possible... but we'll leave that up to you.
Should not have
• - No cheesy "western" fonts or graphics.

```html
<!DOCTYPE html>
<html lang="en">
<head>
<meta charset="utf-8">
<title>Copper Sparrow — Harbors — Disc Label</title>
<link rel="stylesheet" href="https://fonts.googleapis.com/css2?family=Federo&family=Raleway:wght@200;400&family=Arimo:wght@400&display=swap">
<style>
  :root {
    --paper: #ffffff;
    --navy: #2c3447;
    --spine: #1e2433;
    --teal: #1c9dc4;
    --cyan-line: #2fa8dc;
    --magenta: #e0208c;
    --grid: #9aa1ab;
    --white: #f4f5f7;
    --crop: #222222;
  }
  html, body {
    margin: 0;
    padding: 0;
    width: 1200px;
    height: 1200px;
    overflow: hidden;
    background: var(--paper);
  }
  .label-sheet {
    position: relative;
    width: 1200px;
    height: 1200px;
  }
  .label-art {
    position: absolute;
    inset: 0;
  }
  .album-title {
    position: absolute;
    left: 556px;
    top: 352px;
    width: 420px;
    margin: 0;
    font: 200 74px/1 "Raleway", sans-serif;
    letter-spacing: 12px;
    color: var(--white);
    text-align: center;
  }
  .tracklist-motif {
    position: absolute;
    left: 701px;
    top: 437px;
    width: 230px;
    height: 436px;
    box-sizing: border-box;
    border: 2px solid var(--grid);
    background: linear-gradient(180deg, rgba(154,161,171,0.14), rgba(154,161,171,0.06));
  }
  .spec-note {
    position: absolute;
    left: 76px;
    top: 1010px;
    color: var(--cyan-line);
    font-family: "Arimo", sans-serif;
  }
  .spec-note h2 {
    margin: 0 0 6px;
    font-weight: 400;
    font-size: 27px;
    letter-spacing: 2px;
  }
  .spec-note p {
    margin: 0;
    font-size: 18px;
    line-height: 1.3;
  }
  .legend {
    position: absolute;
    left: 898px;
    top: 1016px;
    margin: 0;
    padding: 0;
    list-style: none;
    font-family: "Arimo", sans-serif;
    font-size: 14px;
    line-height: 21px;
  }
  .legend li { display: flex; align-items: center; gap: 6px; }
  .legend .swatch { width: 80px; height: 0; }
  .legend .disc-surface { color: var(--cyan-line); }
  .legend .disc-surface .swatch { border-top: 1.5px solid var(--cyan-line); }
  .legend .text-safety { color: var(--magenta); }
  .legend .text-safety .swatch { border-top: 1.5px dashed var(--magenta); width: 60px; }
  .legend .white-border { color: var(--white); }
  .legend .white-border .swatch { border-top: 4px solid #d8dade; width: 70px; }
  .legend .note { color: var(--white); font-style: italic; font-size: 12px; padding-left: 18px; line-height: 14px; }
</style>
</head>
<body>
<main class="label-sheet">
  <svg class="label-art" width="1200" height="1200" viewBox="0 0 1200 1200">
    <defs>
      <radialGradient id="navy-wash" cx="50%" cy="45%" r="70%">
        <stop offset="0" stop-color="#313a4f"/>
        <stop offset="1" stop-color="#262d3f"/>
      </radialGradient>
      <linearGradient id="spine-fold" x1="0" x2="1" y1="0" y2="0">
        <stop offset="0" stop-color="#232a3b" stop-opacity="0"/>
        <stop offset="0.55" stop-color="#1b2130" stop-opacity="0.9"/>
        <stop offset="1" stop-color="#2a3245" stop-opacity="0.6"/>
      </linearGradient>
    </defs>

    <rect class="label-ground" x="72" y="46" width="1058" height="1108" fill="url(#navy-wash)"/>
    <rect class="spine-fold" x="448" y="46" width="46" height="1108" fill="url(#spine-fold)"/>

    <circle class="disc-surface" cx="600" cy="600" r="530" fill="none" stroke="var(--cyan-line)" stroke-width="2"/>
    <circle class="text-safety" cx="600" cy="600" r="512" fill="none" stroke="var(--magenta)" stroke-width="2" stroke-dasharray="10 8"/>
    <circle class="inner-hole" cx="600" cy="600" r="90" fill="none" stroke="var(--cyan-line)" stroke-width="2"/>
    <circle class="inner-safety" cx="600" cy="600" r="104" fill="none" stroke="var(--magenta)" stroke-width="2" stroke-dasharray="10 8"/>

    <text class="band-name" transform="translate(378 648) rotate(-90)" text-anchor="middle"
          font-family="Federo, sans-serif" font-size="108" fill="var(--teal)"
          textLength="880" lengthAdjust="spacingAndGlyphs">COPPER SPARROW</text>

    <g class="crop-marks" fill="none" stroke="var(--crop)" stroke-width="1.5">
      <circle cx="580" cy="34" r="19"/><line x1="580" y1="0" x2="580" y2="70"/><line x1="540" y1="34" x2="620" y2="34"/>
      <circle cx="580" cy="1166" r="19"/><line x1="580" y1="1130" x2="580" y2="1200"/><line x1="540" y1="1166" x2="620" y2="1166"/>
      <circle cx="34" cy="600" r="19"/><line x1="0" y1="600" x2="70" y2="600"/><line x1="34" y1="560" x2="34" y2="640"/>
      <circle cx="1164" cy="600" r="19"/><line x1="1130" y1="600" x2="1200" y2="600"/><line x1="1164" y1="560" x2="1164" y2="640"/>
    </g>
  </svg>

  <h1 class="album-title">HARBORS</h1>

  <div class="tracklist-motif" role="img" aria-label="Decorative tracklist tile motif with song initials and numbers"></div>

  <section class="spec-note">
    <h2>LABEL</h2>
    <p>DIAMETER 4.6654"</p>
    <p>INNER HOLE: 0.8661"</p>
  </section>

  <ul class="legend">
    <li class="disc-surface">DISC SURFACE <span class="swatch"></span></li>
    <li class="text-safety">TEXT SAFETY <span class="swatch"></span></li>
    <li class="white-border">WHITE BORDER <span class="swatch"></span></li>
    <li class="note">(glossy only)</li>
  </ul>
</main>
</body>
</html>
```